Business card design based on existing website

Please make a business card that is consistent with the look and feel of my new website: http://tellbury.com.sg. By going to the site, I think you'll have all you need in terms of the work I do and the colors I use.

I would like to ask the winner of this project to then do a separate project to design my stationery.

Target Market(s)

Heads of human resources, people wanting psychotherapy, and executives wanting coaching. (It's quite a mix!)

Industry/Entity Type

Psychology

Contact Information for Business Card

Email: ray5678@tellbury.com.sg
Website: http://tellbury.com.sg
Tel: +65 94706218

(I will not have a physical address on the card)

Font styles to use
Serif

Colors

Designer to choose colors to be used in the design.

Requirements
Must have
• On the Front
• ==========
• Have "Dr. Raymond Tellbury" using the font of the website.
• Also "Executive Coach, Psychotherapist, Leadership Professor"
• The back should mention
• ==================
• My degrees
• -------------
• "PhD Kelworth; Post Doc Drayfield". E.g., "Raymond Tellbury (PhD Kelworth; Post Doc Drayfield)" where the text between brackets was in smaller font.
• My work
• ----------
• "Executive coach, psychotherapist, and leadership professor"
• My job titles
• ---------------
• "Principal (Tellbury Consulting)
• Adjunct Professor (Lornvale Commerce University)
• Adjunct Associate Professor (Pemberly Institute of Letters)
• Coach & Supervisor (OKTRAV) '
• Options:
• 1) you can abbreviate Adjunct Professor to "Adj Prof" or "Adj Professor"; and "Adjunct Associate Professor" to "Adj Assoc Prof"
• 2) you abbreviate "Pemberly Institute of Letters" and "Lornvale Commerce University" to "PIL" and "LCU"
• 3) You can also combine the titles for PIL and LCU, e.g., "Adjunct faculty (PIL & LCU)
Nice to have
• Because I work with many Chinese people, it is sometimes helpful to have my family name, "Tellbury", in caps. In the past I have not used caps because it takes away from the aesthetic of the card. Only use caps if it looks good.
• The uploaded image of a "RT" is something that may be helpful. I am undecided.
• THANK YOU for helping me!
Should not have
• No photos. In my industry people consider it overselling.

```html
<!DOCTYPE html>
<html lang="en">
<head>
<meta charset="utf-8">
<title>Dr. Raymond Tellbury – Business Card</title>
<link href="https://fonts.googleapis.com/css2?family=Tinos:wght@400;700&family=Gelasio:ital@1&display=swap" rel="stylesheet">
<style>
  :root {
    --stage-light: #ececec;
    --stage-dark: #c9c9c9;
    --paper: #ffffff;
    --ink: #111111;
    --forest: #1c3a1f;
    --forest-deep: #1f3322;
    --leaf: #5c9a5a;
    --emerald: #0b8a3c;
    --charcoal: #1a261d;
    --rule-light: rgba(255,255,255,0.55);
    --mark-tint: rgba(255,255,255,0.04);
  }
  * { margin: 0; padding: 0; box-sizing: border-box; }
  html, body { width: 1200px; height: 545px; overflow: hidden; }
  body {
    position: relative;
    background: radial-gradient(ellipse at 50% 45%, var(--stage-light) 0%, var(--stage-dark) 100%);
    font-family: "Tinos", "Times New Roman", serif;
  }
  .card {
    position: absolute;
    top: 119px;
    width: 524px;
    height: 307px;
    box-shadow: 0 2px 4px rgba(0,0,0,0.35);
    text-align: center;
    overflow: hidden;
  }
  /* Back side */
  .card--back { left: 68px; background: var(--paper); color: var(--ink); }
  .back__name {
    position: absolute; top: 36px; width: 100%;
    font-size: 27px; font-weight: 400; color: var(--forest); letter-spacing: 0.2px;
  }
  .back__degrees {
    position: absolute; top: 67px; width: 100%;
    font-size: 14.5px; color: var(--leaf);
  }
  .back__services {
    position: absolute; top: 97px; width: 100%;
    font-size: 15px;
  }
  .dot { color: var(--leaf); padding: 0 3px; }
  .back__titles {
    position: absolute; top: 121px; width: 100%;
    list-style: none; font-size: 12.3px; line-height: 18.3px;
  }
  .back__divider {
    position: absolute; top: 209px; left: 107px; width: 308px; height: 1px;
    background: linear-gradient(90deg, rgba(0,0,0,0) 0%, #555 15%, #333 50%, #555 85%, rgba(0,0,0,0) 100%);
  }
  .back__contact {
    position: absolute; top: 225px; width: 100%;
    font-size: 13px; line-height: 20px;
  }
  .back__contact span + span { margin-left: 6px; }
  .back__band {
    position: absolute; left: 0; bottom: 17px; width: 100%; height: 5px;
    background: linear-gradient(90deg, var(--emerald) 0 50%, var(--charcoal) 50% 100%);
  }
  /* Front side */
  .card--front {
    left: 614px; color: #fff;
    background: radial-gradient(ellipse at 50% 40%, #24392a 0%, var(--forest-deep) 70%, #1b2d1e 100%);
  }
  .front__mark {
    position: absolute; top: 22px; left: 122px; width: 254px; height: 254px;
  }
  .front__name {
    position: absolute; top: 96px; width: 100%;
    font-size: 38px; font-weight: 400; letter-spacing: 0.6px;
  }
  .front__rule {
    position: absolute; top: 141px; left: 71px; width: 381px; height: 1px;
    background: var(--rule-light);
  }
  .front__services {
    position: absolute; top: 145px; width: 100%;
    font-size: 24px; line-height: 30px;
  }
  .front__services .dot { color: var(--leaf); font-size: 18px; padding: 0 2px; }
  .front__tagline {
    position: absolute; top: 262px; left: 39px; width: 446px;
    display: flex; align-items: center; gap: 6px;
    font-family: "Gelasio", Georgia, serif; font-style: italic; font-size: 13px;
    color: rgba(255,255,255,0.9);
  }
  .front__tagline::before, .front__tagline::after {
    content: ""; flex: 1; height: 1px; background: var(--rule-light);
  }
</style>
</head>
<body>
  <section class="card card--back">
    <h1 class="back__name">DR. Raymond Tellbury</h1>
    <p class="back__degrees">(PhD Kelworth; Post Doc Drayfield)</p>
    <p class="back__services">Executive coach <span class="dot">•</span> Psychotherapist <span class="dot">•</span> Leadership Professor</p>
    <ul class="back__titles">
      <li>Principal (Tellbury Consulting)</li>
      <li>Adjunct Professor (Lornvale Commerce University)</li>
      <li>Adjunct Associate Professor (Pemberly Institute of Letters)</li>
      <li>Coach &amp; Supervisor (OKTRAV)</li>
    </ul>
    <div class="back__divider"></div>
    <div class="back__contact">
      <p><span>P: +65 94706218</span> <span>E: ray5678@tellbury.com.sg</span></p>
      <p>W: www.tellbury.com.sg</p>
    </div>
    <div class="back__band"></div>
  </section>

  <section class="card card--front">
    <svg class="front__mark" viewBox="0 0 254 254" role="img" aria-label="Faint monogram mark of the practice">
      <rect width="254" height="254" fill="var(--mark-tint)"/>
    </svg>
    <h2 class="front__name">DR. Raymond Tellbury</h2>
    <div class="front__rule"></div>
    <p class="front__services">Executive coach <span class="dot">•</span> Psychotherapist<br>Leadership Professor</p>
    <p class="front__tagline">Advancing Human Development</p>
  </section>
</body>
</html>
```